Homepage Design :) --- A website that connects Journalists to Sources to make brilliant news stories

I need a new homepage designed for a company based in California. The homepage is simple.
The website is BrightQuoteLink.com.

About us:
We are a platform that connects reporters to expert sources (normal people with specific expertise) so a reporter can quickly and easily source information for their news story. Also, the source gets cited in their major news article so it's a win-win situation.

Design:
We have no real slogan except maybe the slogan on the website (beautiful stories that connect us), though that can change too.

I would like to see designs of any style that you choose. We really only have one website color shown in blue on the website, you can use other colors in addition to that one or even change the theme color.

Attachments:
- Homepage to redesign, which you can go to the website yourself to check it out
- A mockup sketch of a revision idea that I had in mind with two people thinking short thoughts. Though this is just a random thought.... You can make anything you want! :)
- An image of what the logged in dashboard looks like just if you want a reference

The footer menu links will remain but can be anything color/style.

Make any ideas you want, keep the same amount of sections or add more, add any graphics or things that you want, etc. I want creativity to really attract customers the second they land on the page. A powerfully beautiful home page!

For reference, some competing websites are NewsWiseDesk.com, Vorlin.io, and plimsa.com
I noticed all these website use red/orange related colors, so maybe I should change the color theme to that? Again, your decision :)

```html
<!DOCTYPE html>
<html lang="en">
<head>
<meta charset="UTF-8">
<title>BrightQuote Link – Home</title>
<link href="https://fonts.googleapis.com/css2?family=Poppins:wght@300;400;500;600;700&display=swap" rel="stylesheet">
<style>
  :root {
    --brand-blue: #0b4f7d;
    --button-blue: #1b5e90;
    --ink: #1b1b1b;
    --white: #ffffff;
    --soft-white: rgba(255,255,255,0.78);
    --footer-text: rgba(255,255,255,0.72);
    --rule: rgba(255,255,255,0.55);
  }
  * { margin: 0; padding: 0; box-sizing: border-box; }
  html, body { width: 1200px; height: 847px; overflow: hidden; background: var(--white); }
  body { font-family: 'Poppins', sans-serif; position: relative; }

  .hero { position: absolute; left: 0; top: 0; width: 1200px; height: 665px; overflow: hidden; }
  .hero-photo {
    position: absolute; inset: 0;
    background:
      radial-gradient(ellipse at 85% 20%, rgba(150,110,95,0.55), transparent 45%),
      linear-gradient(180deg, #d9d9d7 0%, #b8b4ae 22%, #6e6258 48%, #3a332e 72%, #26211e 100%);
  }
  .hero-shade { position: absolute; inset: 0; background: rgba(0,0,0,0.12); }

  .brand { position: absolute; left: 59px; top: 26px; font-weight: 600; font-size: 34px; color: var(--ink); letter-spacing: -0.5px; }
  .main-nav { position: absolute; top: 42px; left: 521px; display: flex; gap: 22px; }
  .main-nav a { font-size: 15.5px; font-weight: 500; color: var(--ink); text-decoration: none; }

  .tagline { position: absolute; top: 143px; left: 0; width: 1200px; text-align: center; color: var(--white); font-size: 26px; font-weight: 500; }
  .headline { position: absolute; top: 187px; left: 0; width: 1200px; text-align: center; color: var(--white); font-size: 36px; font-weight: 400; line-height: 49px; white-space: nowrap; letter-spacing: -0.2px; }

  .cta { position: absolute; top: 372px; height: 34px; width: 249px; background: var(--button-blue); color: var(--white); font-size: 15px; font-weight: 500; display: flex; align-items: center; justify-content: center; border-radius: 2px; opacity: 0.95; }
  .cta-reporter { left: 343px; }
  .cta-source { left: 608px; }

  .about-rule { position: absolute; left: 104px; width: 990px; height: 1px; background: var(--rule); }
  .about-rule.top { top: 468px; }
  .about-rule.bottom { top: 550px; }
  .about-text { position: absolute; top: 485px; left: 100px; width: 1000px; text-align: center; color: var(--soft-white); font-size: 14.5px; line-height: 24px; font-weight: 400; white-space: nowrap; }

  .site-footer { position: absolute; left: 2px; top: 672px; width: 1198px; height: 175px; background: var(--brand-blue); color: var(--white); }
  .footer-brand { position: absolute; left: 253px; top: 28px; font-size: 36px; font-weight: 600; color: var(--white); letter-spacing: -0.5px; }
  .footer-col { position: absolute; top: 20px; }
  .footer-col h4 { font-size: 11px; font-weight: 500; margin-bottom: 10px; }
  .footer-col li { list-style: none; font-size: 10.5px; font-weight: 300; color: var(--footer-text); line-height: 16px; display: flex; align-items: center; gap: 6px; }
  .footer-col.address { left: 552px; }
  .footer-col.menu { left: 805px; }
  .social { position: absolute; left: 988px; top: 43px; display: flex; gap: 10px; }
  .social span { width: 15px; height: 15px; border-radius: 50%; border: 2px solid var(--white); display: block; }
  .copyright { position: absolute; left: 130px; top: 120px; font-size: 11px; font-weight: 600; color: var(--footer-text); display: flex; align-items: center; gap: 5px; }
</style>
</head>
<body>
  <header class="hero">
    <div class="hero-photo" role="img" aria-label="Photo of a press crowd with a camera operator and people raising their hands at a rally"></div>
    <div class="hero-shade"></div>
    <div class="brand">BrightQuote</div>
    <nav class="main-nav">
      <a href="#">How it Works</a>
      <a href="#">About Us</a>
      <a href="#">Signup</a>
      <a href="#">Login</a>
    </nav>
    <h2 class="tagline">Beautiful Stories That Connect Us</h2>
    <h1 class="headline">Find sources for the stories that you need<br>information. Browse profiles of your sources to verify<br>expertise. Explore pitches to discover new topics.</h1>
    <a class="cta cta-reporter">Reporter Signup</a>
    <a class="cta cta-source">Source Signip</a>
    <div class="about-rule top"></div>
    <p class="about-text">We are a platform that connects reporters to expert sources (normal people with specific expertise) so a reporter can quickly and<br>easily source information for their news story. Also, the source gets cited in their major news article so it's a win-win situation.</p>
    <div class="about-rule bottom"></div>
  </header>

  <footer class="site-footer">
    <div class="footer-brand">BrightQuote</div>
    <div class="footer-col address">
      <h4>Address</h4>
      <ul>
        <li><svg width="11" height="11" viewBox="0 0 24 24"><path fill="#fff" d="M6.6 10.8a15 15 0 0 0 6.6 6.6l2.2-2.2a1 1 0 0 1 1-.25 11.4 11.4 0 0 0 3.6.57 1 1 0 0 1 1 1V20a1 1 0 0 1-1 1A17 17 0 0 1 3 4a1 1 0 0 1 1-1h3.5a1 1 0 0 1 1 1c0 1.25.2 2.45.57 3.57a1 1 0 0 1-.25 1z"/></svg>0000-000-0000</li>
        <li><svg width="13" height="10" viewBox="0 0 26 20"><rect x="1" y="1" width="24" height="18" rx="2" fill="#fff"/><path d="M2 3l11 8 11-8" stroke="#0b4f7d" stroke-width="2" fill="none"/></svg>examle@example.com</li>
        <li>address</li>
      </ul>
    </div>
    <div class="footer-col menu">
      <h4>Menu</h4>
      <ul>
        <li>How it Works</li>
        <li>About Us</li>
        <li>Sign Up</li>
        <li>Log In</li>
      </ul>
    </div>
    <div class="social" aria-label="Social links">
      <span></span><span></span><span></span>
    </div>
    <div class="copyright">
      <svg width="12" height="12" viewBox="0 0 24 24"><circle cx="12" cy="12" r="10" stroke="#fff" stroke-opacity="0.72" stroke-width="2" fill="none"/><path d="M15 9a4 4 0 1 0 0 6" stroke="#fff" stroke-opacity="0.72" stroke-width="2" fill="none"/></svg>
      2023 | All Rights Reserved
    </div>
  </footer>
</body>
</html>
```